Eastgate AR Outfitters

Firearms Website

Requirements
Must have
• we are looking for two or three pages for a new company we are starting. The Name is Eastgate Arkansas Outfitters. The site will be EastgateArOutfitters.example (nothing on site at this time) We will be selling mainly handguns and products for self defense. We want this site to focus on the handgun and ammo sells as well as low cost transfers. we will handle the ecommerce part) We want a

1.) main page, mainly general information on the company.

2.) a page for sells. we will be adding the guns by hand as we place them for sell and use our credit card process. We just need the layout to fill in the items for sale on this page.

3.) navigation will be.. HOME - SALES (((guns and gun Accessories)) and self defense products) - Contact US- Transfers

company info

Eastgate Arkansas Outfitters

EastgateAROutfitters.example

sales@EastgateAROutfitters.example

855-Tool 2 Shop (855-555-0142) same number for fax

412 west Harlan avenue

Kosciusko, ms. 71234

```html
<!DOCTYPE html>
<html lang="en">
<head>
<meta charset="utf-8">
<title>Eastgate Arkansas Outfitters</title>
<link href="https://fonts.googleapis.com/css2?family=Ultra&family=Oswald:wght@600&family=Raleway:wght@500&display=swap" rel="stylesheet">
<style>
  :root {
    --backdrop: #0d0d0d;
    --panel: #1c1c1c;
    --panel-dark: #111;
    --nav-top: #3a3a3a;
    --nav-bottom: #141414;
    --accent: #e0150b;
    --accent-bright: #ff2a10;
    --text: #f2f2f2;
    --muted: #d8d8d8;
    --divider: #050505;
  }
  * { margin: 0; padding: 0; box-sizing: border-box; }
  html, body { width: 1200px; height: 1000px; overflow: hidden; }
  body {
    position: relative;
    background:
      repeating-linear-gradient(90deg, rgba(255,255,255,0.025) 0 1px, transparent 1px 4px),
      radial-gradient(ellipse at center, #262626 0%, var(--backdrop) 75%);
    font-family: Arial, Helvetica, sans-serif;
    color: var(--text);
  }
  .page {
    position: absolute; left: 222px; top: 30px; width: 784px; height: 935px;
    background:
      repeating-linear-gradient(90deg, rgba(255,255,255,0.035) 0 1px, transparent 1px 3px),
      linear-gradient(180deg, #262626, var(--panel) 40%, #161616);
  }
  .site-header { position: absolute; left: 0; top: 0; width: 100%; height: 113px; }
  .brand {
    position: absolute; left: 44px; top: 34px; width: 256px;
    font-family: "Oswald", sans-serif; font-weight: 600;
    font-size: 27px; line-height: 1.05; color: var(--text);
    text-transform: uppercase; letter-spacing: 0.5px;
  }
  .tagline {
    position: absolute; left: 360px; top: 50px;
    font-family: "Raleway", sans-serif; font-weight: 500;
    font-size: 15px; letter-spacing: 3.2px; color: var(--muted);
  }
  .cart-tab {
    position: absolute; right: 26px; top: 0; width: 34px; height: 30px;
    background: var(--accent); border-radius: 0 0 8px 8px;
  }
  .cart-tab svg { position: absolute; left: 8px; top: 7px; }
  .main-nav {
    position: absolute; left: 0; top: 113px; width: 100%; height: 44px;
    background: linear-gradient(180deg, var(--nav-top), var(--nav-bottom));
    border-bottom: 1px solid #000;
  }
  .main-nav ul { list-style: none; position: absolute; left: 115px; top: 0; display: flex; height: 44px; }
  .main-nav li {
    height: 44px; display: flex; align-items: center; justify-content: center;
    font-size: 15px; letter-spacing: 1px; color: var(--text);
    border-right: 2px solid var(--divider);
  }
  .main-nav li.is-active {
    background: linear-gradient(180deg, var(--accent-bright), #b90f06);
  }
  .hero { position: absolute; left: 0; top: 157px; width: 100%; height: 570px; overflow: hidden; }
  .hero-photo {
    position: absolute; inset: 0;
    background:
      linear-gradient(172deg, #7a7a7a 0%, #2a2a2a 14%, #0a0a0a 30%, #222 45%, #050505 60%, #3a3a3a 75%, #1a1a1a 100%);
  }
  .hero-words { position: absolute; left: 0; top: 0; }
  .hero-words text {
    font-family: "Ultra", serif; fill: var(--accent-bright); opacity: 0.82;
  }
  .site-footer {
    position: absolute; left: 0; top: 778px; width: 100%; text-align: center;
  }
  .footer-links { font-size: 17px; letter-spacing: 0.6px; color: var(--text); padding-left: 30px; }
  .footer-links .sep { margin: 0 9px; }
  .copyright { margin-top: 6px; font-size: 13.5px; color: var(--muted); padding-left: 30px; }
</style>
</head>
<body>
  <div class="page">
    <header class="site-header">
      <div class="brand">Eastgate Arkansas Outfitters</div>
      <div class="tagline">GUNS - ACCESSORIES - SELF DEFENSE</div>
      <div class="cart-tab">
        <svg width="18" height="16" viewBox="0 0 18 16" fill="none" stroke="#fff" stroke-width="1.6">
          <path d="M1 2h3l2 8h9l2-6H5"/>
          <circle cx="7" cy="13.5" r="1.3" fill="#fff"/>
          <circle cx="14" cy="13.5" r="1.3" fill="#fff"/>
        </svg>
      </div>
    </header>

    <nav class="main-nav">
      <ul>
        <li class="is-active" style="width:118px">Home</li>
        <li style="width:116px">Sales</li>
        <li style="width:153px">Contact Us</li>
        <li style="width:148px">Transfers</li>
      </ul>
    </nav>

    <section class="hero">
      <div class="hero-photo" role="img" aria-label="Black and white photograph of a handgun, a pile of ammunition and a river bridge at dusk"></div>
      <svg class="hero-words" width="784" height="570" viewBox="0 0 784 570">
        <text x="11" y="168" font-size="112" textLength="742" lengthAdjust="spacingAndGlyphs">HANDGUNS</text>
        <text x="293" y="323" font-size="118" textLength="470" lengthAdjust="spacingAndGlyphs">AMMO</text>
        <text x="63" y="473" font-size="100" textLength="620" lengthAdjust="spacingAndGlyphs">LOW COST</text>
        <text x="11" y="553" font-size="100" textLength="762" lengthAdjust="spacingAndGlyphs">TRANSFERS</text>
      </svg>
    </section>

    <footer class="site-footer">
      <div class="footer-links">Home<span class="sep">|</span>Sales<span class="sep">|</span>Contact Us<span class="sep">|</span>Transfers</div>
      <div class="copyright">Copyrights © 2013 All Rights Reserved</div>
    </footer>
  </div>
</body>
</html>
```